Snack package design "Lantern Curl Bites"

Looking to create a fun package design of snack. Snack is sweet and crunchy; great for people that wants to munch on stuff. Name of the Snack is "Lantern Curl Bites". The net weight should be 16oz (453 grams). I added brand "TWbR" Tiny Wonders bring Rain on the file. I also added picture of the snack. Package will be a pouch type.

Target Market(s)

People that like sweet snacks

Industry/Entity Type

Food snacks

Requirements
Must have
• Name of Snack "Lantern Curl Bites" and logo of company on top left.
Nice to have
• something that's simple and clean design

```html
<!DOCTYPE html>
<html lang="en">
<head>
<meta charset="UTF-8">
<title>Lantern Curl Bites – Pouch Front</title>
<link href="https://fonts.googleapis.com/css2?family=Bebas+Neue&display=swap" rel="stylesheet">
<style>
  :root {
    --pouch-red: #e30b25;
    --blush-pink: #f2a7b0;
    --cocoa-ink: #3b2a2a;
    --snack-light: #e3a65e;
    --snack-deep: #b4672c;
    --page-white: #ffffff;
  }
  * { box-sizing: border-box; margin: 0; padding: 0; }
  html, body {
    width: 1200px;
    height: 1200px;
    overflow: hidden;
    background: var(--page-white);
  }
  .pouch-front {
    position: absolute;
    left: 220px;
    top: 40px;
    width: 760px;
    height: 1120px;
    background: var(--pouch-red);
    overflow: hidden;
    font-family: "Bebas Neue", "Arial Narrow", sans-serif;
  }
  .brand-mark {
    position: absolute;
    left: 68px;
    top: 52px;
    display: flex;
    align-items: center;
    gap: 12px;
    color: var(--page-white);
  }
  .brand-dot {
    width: 38px;
    height: 38px;
    border-radius: 50%;
    background: var(--blush-pink);
  }
  .brand-name {
    font-size: 52px;
    line-height: 1;
    letter-spacing: 2px;
  }
  .brand-tagline {
    position: absolute;
    left: 68px;
    top: 112px;
    font-size: 22px;
    letter-spacing: 1px;
    color: var(--page-white);
  }
  .product-title {
    position: absolute;
    left: 76px;
    top: 160px;
    font-size: 158px;
    line-height: 134px;
    font-weight: 400;
    color: var(--blush-pink);
    letter-spacing: 1px;
    text-shadow:
      1px 1px 0 var(--cocoa-ink), 2px 2px 0 var(--cocoa-ink),
      3px 3px 0 var(--cocoa-ink), 4px 4px 0 var(--cocoa-ink),
      5px 5px 0 var(--cocoa-ink), 6px 6px 0 var(--cocoa-ink),
      7px 7px 0 var(--cocoa-ink);
  }
  .product-title span { display: block; }
  .snack-photo {
    position: absolute;
    left: 0;
    top: 520px;
    width: 760px;
    height: 476px;
    display: block;
  }
  .weight-band {
    position: absolute;
    left: 0;
    bottom: 0;
    width: 760px;
    height: 125px;
    background: var(--blush-pink);
  }
  .net-weight {
    position: absolute;
    right: 70px;
    top: 48px;
    font-size: 36px;
    line-height: 1;
    color: var(--cocoa-ink);
    letter-spacing: 0.5px;
  }
</style>
</head>
<body>
  <main class="pouch-front">
    <div class="brand-mark">
      <span class="brand-dot"></span>
      <span class="brand-name">TWbR</span>
    </div>
    <p class="brand-tagline">Tiny Wonders bring Rain</p>

    <h1 class="product-title">
      <span>Lantern</span>
      <span>Curl</span>
      <span>Bites</span>
    </h1>

    <svg class="snack-photo" viewBox="0 0 760 476" role="img" aria-label="Pile of golden, caramel-glazed curled crunchy snack pieces sprinkled with sesame" preserveAspectRatio="none">
      <defs>
        <linearGradient id="snackTone" x1="0" y1="0" x2="0" y2="1">
          <stop offset="0" stop-color="var(--snack-light)"/>
          <stop offset="1" stop-color="var(--snack-deep)"/>
        </linearGradient>
      </defs>
      <path fill="url(#snackTone)" d="M0 100 L40 92 L60 110 L130 96 L165 70 L230 76 L260 88 L300 66 L345 60 L370 80 L420 70 L450 40 L470 52 L520 36 L560 20 L600 16 L640 42 L680 36 L700 52 L730 44 L760 56 L760 476 L0 476 Z"/>
    </svg>

    <div class="weight-band">
      <p class="net-weight">Net 16oz (453 grams)</p>
    </div>
  </main>
</body>
</html>
```